Vantor Advisory business card

Premium business card required
I have attached the brand as a powerpoint template but this can be made to look very up market, I have also attached my BIO for title reasons and to give you a feel for my skills
front of card
Derek Holloway
Managing Director Vantor Advisory
Retail, Customer-Led Experience, Transformation and Maximising Shareholder Return
Mobile +61(0)418557392
Email derekvantoradvisory.com
back of card

VANTOR ADVISORY’ OFFERING

We transform customer environments to extract benefits while elevating service levels;
We release millions of dollars in self-funding through continuous improvement;
We see CX as a key differentiator, proactively guarding share from market disrupters;
We re-invent service and create front-end of the future.

```html
<!DOCTYPE html>
<html lang="en">
<head>
<meta charset="utf-8">
<title>Vantor Advisory – Business Card</title>
<link rel="stylesheet" href="https://fonts.googleapis.com/css2?family=Work+Sans:wght@400;500&display=swap">
<style>
  :root {
    --backdrop: #d6d6d6;
    --card: #ffffff;
    --brand-grey: #8c8c8c;
    --text-grey: #5a5a5a;
    --rule: #9a9a9a;
  }
  * { margin: 0; padding: 0; box-sizing: border-box; }
  html, body { width: 1200px; height: 800px; overflow: hidden; }
  body {
    background: var(--backdrop);
    font-family: "Work Sans", Arial, sans-serif;
    color: var(--text-grey);
    position: relative;
  }
  .card {
    position: absolute;
    top: 245px;
    width: 540px;
    height: 309px;
    background: var(--card);
    box-shadow: 0 2px 6px rgba(0,0,0,0.18);
  }
  .card--front { left: 40px; }
  .card--back { left: 620px; }

  .brand {
    position: absolute;
    display: flex;
    align-items: center;
    gap: 10px;
    color: var(--brand-grey);
    font-weight: 500;
    font-size: 22px;
    letter-spacing: 3px;
  }
  .brand__square { width: 18px; height: 18px; background: var(--brand-grey); }

  .card--front .brand { top: 48px; right: 44px; }
  .rule { position: absolute; height: 1px; background: var(--rule); }
  .rule--top { top: 102px; right: 44px; width: 300px; }
  .rule--bottom { top: 212px; left: 44px; width: 300px; }

  .contact {
    position: absolute;
    top: 124px;
    right: 44px;
    list-style: none;
    font-size: 14px;
    line-height: 22px;
  }
  .contact li { display: flex; align-items: center; gap: 8px; }
  .contact svg { width: 12px; height: 12px; stroke: var(--text-grey); fill: none; stroke-width: 1.4; }

  .person { position: absolute; top: 224px; left: 44px; font-size: 15px; line-height: 19px; }
  .person__name { color: var(--brand-grey); font-weight: 500; font-size: 17px; letter-spacing: 0.5px; }

  .card--back .brand { top: 44px; left: 44px; }
  .offering { position: absolute; top: 120px; left: 44px; right: 36px; }
  .offering__title {
    color: var(--brand-grey);
    font-weight: 400;
    font-size: 14px;
    letter-spacing: 0.8px;
    margin-bottom: 10px;
  }
  .offering__list { list-style: none; font-size: 11.5px; line-height: 19px; }
  .offering__list li { position: relative; padding-left: 14px; }
  .offering__list li::before {
    content: ""; position: absolute; left: 2px; top: 7px;
    width: 5px; height: 5px; border-radius: 50%; background: var(--brand-grey);
  }
</style>
</head>
<body>
  <section class="card card--front" aria-label="Front of card">
    <div class="brand"><span class="brand__square"></span>VANTOR ADVISORY</div>
    <div class="rule rule--top"></div>
    <ul class="contact">
      <li><svg viewBox="0 0 12 12"><path d="M2 1.5 L4 1.5 L5 4 L3.8 5 Q5 7.5 7 8.2 L8 7 L10.5 8 L10.5 10 Q5 10.5 1.5 3.5 Z"/></svg>+61(0)418557392</li>
      <li><svg viewBox="0 0 12 12"><rect x="1" y="2.5" width="10" height="7"/><path d="M1 2.5 L6 6.5 L11 2.5"/></svg>derekvantoradvisory.com</li>
    </ul>
    <div class="rule rule--bottom"></div>
    <div class="person">
      <p class="person__name">DEREK HOLLOWAY</p>
      <p class="person__title">Managing Director</p>
      <p class="person__company">Vantor Advisory</p>
    </div>
  </section>

  <section class="card card--back" aria-label="Back of card">
    <div class="brand"><span class="brand__square"></span>VANTOR ADVISORY</div>
    <div class="offering">
      <h2 class="offering__title">VANTOR ADVISORY’ OFFERING</h2>
      <ul class="offering__list">
        <li>We transform customer environments to extract benefits while elevating service levels;</li>
        <li>We release millions of dollars in self-funding through continuous improvement;</li>
        <li>We see CX as a key differentiator, proactively guarding share from market disrupters;</li>
        <li>We re-invent service and create front-end of the future.</li>
      </ul>
    </div>
  </section>
</body>
</html>
```